Family Ranch with a hobby vineyard needs 2 wine labels for our first harvest

Design 2 wine labels (front and back) with the Brindor Ranch logo.
Label 1:
Sauvignon Blanc
Alc. 12.5% by Vol.
Palos Verdes Peninsula - add as the region
Year 2022
Label 2:
Cabernet Sauvignon
Alc. 13.5% by Vol.
Year 2022
For the back label design:
GOVERNMENT WARNING: (1) According to the Surgeon General, women
should not drink alcoholic beverages during pregnancy because of the risk of
birth defects. (2) Consumption of alcoholic beverages impairs your ability to
drive a car or operate machinery, and may cause health problems.
Contains Sulfates.
750ML
I just received the bottles and have attached a picture.
Look and feel
Each slider illustrates characteristics of the customer's brand and the style your logo design should communicate.

```html
<!DOCTYPE html>
<html lang="en">
<head>
<meta charset="utf-8">
<title>Brindor Ranch Wine Labels</title>
<link rel="stylesheet" href="https://fonts.googleapis.com/css2?family=Oswald:wght@500;600&family=EB+Garamond:ital,wght@0,400;0,500;1,400&family=Fira+Sans:wght@400&family=Fira+Sans+Condensed:wght@700&display=swap">
<style>
  :root {
    --canvas: #ededeb;
    --charcoal: #2b292b;
    --charcoal-deep: #232123;
    --gold: #d5a02b;
    --gold-soft: #c99a35;
    --white: #f6f6f6;
    --silver-light: #f2f2f2;
    --silver-mid: #a9a9a9;
    --silver-dark: #4a4a4a;
  }
  * { box-sizing: border-box; margin: 0; padding: 0; }
  html, body { width: 1200px; height: 960px; overflow: hidden; }
  body {
    background: var(--canvas);
    display: flex;
    align-items: center;
    justify-content: center;
    gap: 24px;
  }

  /* shared label shell */
  .label {
    width: 272px;
    background: var(--charcoal);
    padding: 12px;
    box-shadow: 0 2px 6px rgba(0,0,0,0.18);
  }
  .label__frame {
    height: 100%;
    padding: 9px;
    background: linear-gradient(90deg, var(--silver-dark) 0%, var(--silver-mid) 12%, var(--silver-dark) 30%, #5a5a5a 55%, var(--silver-light) 85%, var(--silver-mid) 100%);
  }
  .label__panel {
    height: 100%;
    background: var(--charcoal);
    border: 2px solid var(--silver-mid);
    outline: 3px solid var(--charcoal);
    outline-offset: -6px;
    display: flex;
    flex-direction: column;
    align-items: center;
  }

  /* front label */
  .label--front { height: 412px; }
  .front__brand {
    height: 176px;
    display: flex;
    align-items: center;
    justify-content: center;
    font-family: "Oswald", sans-serif;
    font-weight: 500;
    font-size: 27px;
    letter-spacing: 1px;
    text-transform: uppercase;
    color: var(--gold);
  }
  .front__variety {
    font-family: "Oswald", sans-serif;
    font-weight: 600;
    font-size: 25px;
    line-height: 1;
    letter-spacing: -0.3px;
    text-transform: uppercase;
    background: linear-gradient(180deg, var(--white) 30%, #9b9b9b 100%);
    -webkit-background-clip: text;
    background-clip: text;
    color: transparent;
    white-space: nowrap;
  }
  .front__region {
    margin-top: 10px;
    width: calc(100% - 8px);
    background: var(--gold);
    text-align: center;
    font-family: "EB Garamond", serif;
    font-size: 13px;
    line-height: 20px;
    color: var(--charcoal-deep);
    text-transform: uppercase;
  }
  .front__year {
    margin-top: 14px;
    font-family: "Fira Sans Condensed", sans-serif;
    font-weight: 700;
    font-size: 27px;
    line-height: 1;
    color: var(--gold);
    text-transform: uppercase;
  }
  .front__abv {
    margin-top: 6px;
    font-family: "Fira Sans", sans-serif;
    font-size: 14px;
    color: var(--white);
    text-transform: uppercase;
  }

  /* back label */
  .label--back { height: 272px; }
  .back__panel { justify-content: center; padding: 0 12px; text-align: center; }
  .back__title {
    font-family: "EB Garamond", serif;
    font-size: 12.5px;
    letter-spacing: 0.3px;
    color: var(--white);
    text-transform: uppercase;
    margin-bottom: 9px;
  }
  .back__text {
    font-family: "EB Garamond", serif;
    font-style: italic;
    font-size: 9.6px;
    line-height: 1.4;
    color: var(--gold-soft);
  }
  .back__rule {
    width: 136px;
    height: 1px;
    background: var(--gold-soft);
    margin: 8px auto;
  }
  .back__sulfites { margin-top: 10px; }
  .back__volume {
    margin-top: 4px;
    font-family: "EB Garamond", serif;
    font-size: 15px;
    color: var(--gold-soft);
    text-transform: uppercase;
  }
</style>
</head>
<body>

  <section class="label label--front">
    <div class="label__frame">
      <div class="label__panel">
        <div class="front__brand">Brindor Ranch</div>
        <h2 class="front__variety">Sauvignon Blanc</h2>
        <p class="front__region">Palos Verdes Peninsula</p>
        <p class="front__year">Year 2022</p>
        <p class="front__abv">Alc. 12.5% by Vol.</p>
      </div>
    </div>
  </section>

  <section class="label label--front">
    <div class="label__frame">
      <div class="label__panel">
        <div class="front__brand">Brindor Ranch</div>
        <h2 class="front__variety">Cabernet Sauvignon</h2>
        <p class="front__region">Palos Verdes Peninsula</p>
        <p class="front__year">Year 2022</p>
        <p class="front__abv">Alc. 13.5% by Vol.</p>
      </div>
    </div>
  </section>

  <section class="label label--back">
    <div class="label__frame">
      <div class="label__panel back__panel">
        <h3 class="back__title">Government Warning</h3>
        <p class="back__text">According to the Surgeon General, women<br>should not drink alcoholic beverages<br>during pregnancy because of the risk of<br>birth defects.</p>
        <div class="back__rule"></div>
        <p class="back__text">Consumption of alcoholic beverages<br>impairs your ability to<br>drive a car or operate machinery, and may<br>cause health problems.</p>
        <p class="back__text back__sulfites">Contains Sulfates.</p>
        <p class="back__volume">750ml</p>
      </div>
    </div>
  </section>

  <section class="label label--back">
    <div class="label__frame">
      <div class="label__panel back__panel">
        <h3 class="back__title">Government Warning</h3>
        <p class="back__text">According to the Surgeon General, women<br>should not drink alcoholic beverages<br>during pregnancy because of the risk of<br>birth defects.</p>
        <div class="back__rule"></div>
        <p class="back__text">Consumption of alcoholic beverages<br>impairs your ability to<br>drive a car or operate machinery, and may<br>cause health problems.</p>
        <p class="back__text back__sulfites">Contains Sulfates.</p>
        <p class="back__volume">750ml</p>
      </div>
    </div>
  </section>

</body>
</html>
```